Need Bold, Hip Card for Concert Ticket Website Velvet Stubs!

Hi there! I am putting together a business/website that sells event tickets (mostly concerts, but also some sports and theater). Think PassDepot, but much smaller. The site is called Velvet Stubs. I have a new logo (attached, with black/red/white color scheme), and am looking for a modern/cool/original business card design. Note that I am thinking of having the card itself in the shape of a ticket (die cut), so you may want to keep that in mind when designing, but I'm not set on that. I'm also open to alternative card sizes, thicknesses, glossy, spot UV, etc. in order to stand out. I'm attaching a potential die cut template and a sample card using that template in case you want to work with that.
Target Market(s)
Music fans, people that like going to see live events
Industry/Entity Type
Entertainment
Contact Information for Business Card
Information that I'd like to have:
website address - www.velvetstubs-example.com
phone number: 1-833-5VELVETS (835-3887)
my name - Delia Hart
Look and feel
Each slider illustrates characteristics of the customer's brand and the style your logo design should communicate.

```html
<!DOCTYPE html>
<html lang="en">
<head>
<meta charset="UTF-8">
<title>Velvet Stubs — Business Card</title>
<link href="https://fonts.googleapis.com/css2?family=Montserrat:wght@400;500;800&display=swap" rel="stylesheet">
<style>
  :root {
    --stage: #ecebe8;
    --velvet-red: #8e1c22;
    --deep-red: #7a141a;
    --ink: #2b2b2b;
    --gloss: #1e1e1e;
    --paper: #ffffff;
    --faint: #f1efef;
    --muted: #555555;
  }
  * { box-sizing: border-box; margin: 0; padding: 0; }
  html, body {
    width: 1200px; height: 800px; overflow: hidden;
    background: var(--stage);
    font-family: "Montserrat", Arial, sans-serif;
  }
  .canvas {
    position: relative; width: 1200px; height: 800px;
  }
  .ticket-card {
    position: absolute; left: 290px; width: 620px; height: 350px;
  }
  .ticket-card--front { top: 40px; }
  .ticket-card--back { top: 410px; }
  .ticket-shape {
    position: absolute; inset: 0; width: 100%; height: 100%;
    filter: drop-shadow(0 6px 10px rgba(0,0,0,0.18));
  }
  .ticket-shape--front path { fill: var(--velvet-red); }
  .ticket-shape--back path { fill: var(--paper); }

  /* Front */
  .brand-lockup {
    position: absolute; left: 0; right: 0; top: 0; bottom: 0;
    display: flex; align-items: center; justify-content: center; gap: 16px;
  }
  .brand-square {
    width: 40px; height: 40px; background: var(--gloss);
  }
  .brand-name {
    font-weight: 800; font-size: 52px; letter-spacing: 1px;
    color: var(--gloss); text-transform: uppercase;
  }

  /* Back */
  .faint-mark {
    position: absolute; right: 70px; top: 26px; width: 190px; height: 150px;
    background: var(--faint); border-radius: 6px;
  }
  .back-brand {
    position: absolute; left: 60px; top: 58px;
    display: flex; align-items: center; gap: 10px;
  }
  .back-brand .brand-square { width: 24px; height: 24px; background: var(--deep-red); }
  .back-brand .brand-name { font-size: 30px; color: var(--deep-red); }
  .holder-name {
    position: absolute; left: 0; right: 0; top: 146px; text-align: center;
    font-weight: 400; font-size: 30px; color: var(--ink);
  }
  .contact-row {
    position: absolute; left: 60px; right: 50px;
    display: flex; justify-content: space-between; align-items: center;
    font-size: 14px; color: var(--muted);
  }
  .contact-row--upper { top: 236px; }
  .contact-row--lower { top: 276px; }
  .rule {
    position: absolute; left: 60px; right: 50px; top: 262px;
    height: 2px; background: var(--deep-red);
  }
  .contact-item { display: flex; align-items: center; gap: 8px; }
  .contact-icon { width: 16px; height: 16px; fill: var(--deep-red); }
  .website { color: var(--deep-red); font-weight: 500; }
  .social-list { display: flex; gap: 8px; }
  .social-square { width: 16px; height: 16px; background: var(--deep-red); border-radius: 2px; }
</style>
</head>
<body>
<main class="canvas">

  <section class="ticket-card ticket-card--front">
    <svg class="ticket-shape ticket-shape--front" viewBox="0 0 620 350" aria-hidden="true">
      <path d="M30 0 H590 A30 30 0 0 0 620 30 V320 A30 30 0 0 0 590 350 H30 A30 30 0 0 0 0 320 V30 A30 30 0 0 0 30 0 Z"/>
    </svg>
    <div class="brand-lockup">
      <span class="brand-square"></span>
      <span class="brand-name">Velvet Stubs</span>
    </div>
  </section>

  <section class="ticket-card ticket-card--back">
    <svg class="ticket-shape ticket-shape--back" viewBox="0 0 620 350" aria-hidden="true">
      <path d="M30 0 H590 A30 30 0 0 0 620 30 V320 A30 30 0 0 0 590 350 H30 A30 30 0 0 0 0 320 V30 A30 30 0 0 0 30 0 Z"/>
    </svg>
    <div class="faint-mark"></div>
    <div class="back-brand">
      <span class="brand-square"></span>
      <span class="brand-name">Velvet Stubs</span>
    </div>
    <p class="holder-name">Delia Hart</p>

    <div class="contact-row contact-row--upper">
      <span class="contact-item">
        <svg class="contact-icon" viewBox="0 0 24 24" aria-hidden="true"><path d="M6.6 10.8a15.1 15.1 0 0 0 6.6 6.6l2.2-2.2a1 1 0 0 1 1-.25 11.4 11.4 0 0 0 3.6.57 1 1 0 0 1 1 1V20a1 1 0 0 1-1 1A17 17 0 0 1 3 4a1 1 0 0 1 1-1h3.5a1 1 0 0 1 1 1c0 1.25.2 2.45.57 3.57a1 1 0 0 1-.25 1z"/></svg>
        1-833-5VELVETS (835-3887)
      </span>
      <span class="contact-item">
        <svg class="contact-icon" viewBox="0 0 24 24" aria-hidden="true"><path d="M2 5h20v14H2z M2 5l10 8 10-8" fill="none" stroke="#7a141a" stroke-width="2"/></svg>
        delia@velvetstubs-example.com
      </span>
    </div>
    <div class="rule"></div>
    <div class="contact-row contact-row--lower">
      <span class="website">www.velvetstubs-example.com</span>
      <span class="social-list">
        <span class="social-square"></span>
        <span class="social-square"></span>
        <span class="social-square"></span>
      </span>
    </div>
  </section>

</main>
</body>
</html>
```